Business Card for a Floral & Decorating Business

I would like to take my current logo and create a better business card. I am looking for elegance as I am a florist and event decorator. My logo has multiple colour options. I like colours like green, purple, pink and orange, I think I would like a white card, open to black back ground. I want it to feel elegant and romantic. I like metallic lettering that maybe is indented in the paper, I also like glossy paper. I have a full logo already as well as a badge. I have attached both in multiple colours.m
Updates

Need extra days to review

Target Market(s)

Weddings, special events, floral customers

Industry/Entity Type

Floral and decorating

Contact Information for Business Card

Phone number, email, instagram, facebook, title, name, logo

Font styles to use
Script

Requirements
Nice to have
• Elegant

```html
<!DOCTYPE html>
<html lang="en">
<head>
<meta charset="utf-8">
<title>Marlowe Blooms – Business Card</title>
<link rel="stylesheet" href="https://fonts.googleapis.com/css2?family=Great+Vibes&family=Montserrat:wght@400;500&display=swap">
<style>
  :root {
    --backdrop: #1c1c1c;
    --card: #1a1a1a;
    --card-edge: #262626;
    --gold: #e2b43a;
    --gold-soft: #c99a2e;
    --ink: #ffffff;
    --pattern: #2c2c2c;
  }
  * { margin: 0; padding: 0; box-sizing: border-box; }
  html, body { width: 1200px; height: 900px; overflow: hidden; }
  body {
    background: var(--backdrop);
    display: flex;
    flex-direction: column;
    align-items: center;
    justify-content: center;
    gap: 40px;
    font-family: "Montserrat", sans-serif;
  }
  .card {
    position: relative;
    width: 700px;
    height: 400px;
    background: var(--card);
    border: 1px solid var(--card-edge);
    overflow: hidden;
    box-shadow: 0 18px 40px rgba(0,0,0,0.55);
  }
  .card-pattern {
    position: absolute;
    inset: 0;
    background: linear-gradient(100deg, var(--card) 0%, var(--card) 45%, var(--pattern) 100%);
  }
  /* Front */
  .badge {
    position: absolute;
    left: 50%;
    top: 50%;
    width: 280px;
    height: 280px;
    transform: translate(-50%, -50%);
    border: 2px solid var(--gold);
    border-radius: 50%;
    display: flex;
    align-items: center;
    justify-content: center;
  }
  .brand-name {
    font-family: "Montserrat", sans-serif;
    font-weight: 500;
    font-size: 26px;
    letter-spacing: 3px;
    color: var(--gold);
    text-transform: uppercase;
    text-align: center;
    line-height: 1.3;
  }
  /* Back */
  .back-content {
    position: absolute;
    inset: 0;
    display: flex;
    flex-direction: column;
    align-items: center;
  }
  .social {
    margin-top: 58px;
    display: flex;
    align-items: center;
    gap: 10px;
    color: var(--ink);
  }
  .social-dot {
    width: 14px; height: 14px;
    border-radius: 50%;
    background: var(--gold);
  }
  .social-handle {
    font-family: "Great Vibes", cursive;
    font-size: 28px;
  }
  .person-name {
    margin-top: 48px;
    font-family: "Great Vibes", cursive;
    font-size: 60px;
    color: var(--gold);
    line-height: 1;
  }
  .person-title {
    margin-top: 2px;
    font-size: 18px;
    color: var(--ink);
    letter-spacing: 0.5px;
  }
  .contact {
    margin-top: 52px;
    font-size: 20px;
    color: var(--ink);
    line-height: 1.45;
    letter-spacing: 0.5px;
  }
  .contact-label { color: var(--gold); font-weight: 500; margin-right: 6px; }
</style>
</head>
<body>
  <section class="card card-front">
    <div class="card-pattern" role="img" aria-label="Faint dark geometric petal pattern across the card"></div>
    <div class="badge">
      <span class="brand-name">Marlowe<br>Blooms</span>
    </div>
  </section>

  <section class="card card-back">
    <div class="card-pattern" role="img" aria-label="Faint dark geometric petal pattern across the card"></div>
    <div class="back-content">
      <div class="social">
        <span class="social-dot"></span>
        <span class="social-handle">/ marloweblooms</span>
      </div>
      <div class="person-name">Julian Hartley</div>
      <div class="person-title">Director</div>
      <div class="contact">
        <div><span class="contact-label">P:</span>(555) 214-0387</div>
        <div><span class="contact-label">E:</span>hello@marloweblooms.com</div>
      </div>
    </div>
  </section>
</body>
</html>
```